Building Company Business Card Design

Need a design for a business card:
It needs to have: Name, Phone, Facebook link, Website, email
i would also like a list of works we undertake:
-New Homes
-Extensions, Renovations & Bathrooms
-Decking, Carports, Sheds (Residential and Industrial)
-Carpentry
-Fences, Patios & Pergolas

Name, Phone, Facebook link, Website, email + details of services provided listed in description

```html
<!DOCTYPE html>
<html lang="en">
<head>
<meta charset="utf-8">
<title>Ridgeline Homes – Business Card</title>
<link rel="stylesheet" href="https://fonts.googleapis.com/css2?family=Lato:wght@400;700;900&display=swap">
<style>
  :root {
    --brand-green: #37b34a;
    --ink: #1d1d1f;
    --muted-grey: #8a8a8a;
    --card-white: #ffffff;
    --backdrop: #2a2a2d;
  }
  * { box-sizing: border-box; margin: 0; padding: 0; }
  html, body { width: 1200px; height: 947px; overflow: hidden; }
  body {
    background: var(--backdrop);
    font-family: "Lato", Arial, sans-serif;
    color: var(--ink);
    position: relative;
  }
  .card {
    position: absolute;
    width: 640px;
    height: 366px;
    background: var(--card-white);
    border-radius: 18px;
    overflow: hidden;
  }
  .card--front { left: 120px; top: 80px; }
  .card--back { left: 440px; top: 500px; }
  .card__bands { position: absolute; inset: 0; width: 100%; height: 100%; }

  .company-name { position: absolute; }
  .company-name__title {
    font-weight: 900;
    font-size: 32px;
    letter-spacing: 1px;
    color: var(--ink);
    display: flex;
    align-items: center;
    gap: 10px;
    line-height: 1;
  }
  .company-name__mark {
    width: 22px; height: 22px;
    background: var(--brand-green);
    display: inline-block;
  }
  .company-name__sub {
    font-weight: 900;
    font-size: 13px;
    letter-spacing: 2.2px;
    color: var(--ink);
    margin: 6px 0 0 32px;
  }
  .card--front .company-name { left: 40px; top: 200px; }
  .card--back .company-name { left: 40px; top: 36px; }

  .contact { position: absolute; left: 360px; top: 42px; }
  .contact__name { color: var(--brand-green); font-weight: 900; font-size: 30px; line-height: 1.05; }
  .contact__role { font-size: 15px; margin: 4px 0 14px; }
  .contact__list { list-style: none; }
  .contact__item {
    display: flex; align-items: center; gap: 10px;
    font-size: 16px; line-height: 1.55;
  }
  .contact__icon { width: 14px; height: 14px; flex: none; }

  .social-handle {
    position: absolute;
    color: #fff;
    font-size: 18px;
    display: flex; align-items: center; gap: 8px;
  }
  .social-handle__dot { width: 18px; height: 18px; border-radius: 50%; background: #fff; }
  .card--front .social-handle { right: 36px; bottom: 22px; }
  .card--back .social-handle { right: 36px; bottom: 22px; }

  .services { position: absolute; left: 48px; top: 116px; }
  .services__heading { color: var(--brand-green); font-weight: 900; font-size: 26px; line-height: 1.2; margin-bottom: 8px; }
  .services__list { list-style: none; }
  .services__item {
    display: flex; align-items: center; gap: 14px;
    font-size: 18px; line-height: 1.36;
  }
  .services__bullet { width: 12px; height: 12px; background: var(--brand-green); flex: none; }
</style>
</head>
<body>

<section class="card card--front" aria-label="Business card front">
  <svg class="card__bands" viewBox="0 0 640 366" aria-hidden="true">
    <polygon points="0,352 340,352 350,340 640,340 640,366 0,366" fill="var(--muted-grey)"/>
    <polygon points="340,366 392,300 640,300 640,366" fill="var(--brand-green)"/>
  </svg>

  <div class="company-name">
    <div class="company-name__title"><span class="company-name__mark"></span>RIDGELINE HOMES</div>
    <div class="company-name__sub">AND DEVELOPMENTS PTY LTD</div>
  </div>

  <div class="contact">
    <div class="contact__name">Morgan Ellery</div>
    <div class="contact__role">Manager</div>
    <ul class="contact__list">
      <li class="contact__item">
        <svg class="contact__icon" viewBox="0 0 16 16" aria-hidden="true"><path d="M3 1l3 3-2 2c1 2 3 4 5 5l2-2 3 3-2 2C7 14 2 9 1 3z" fill="var(--brand-green)"/></svg>
        1 555 010 4821
      </li>
      <li class="contact__item">
        <svg class="contact__icon" viewBox="0 0 16 16" aria-hidden="true"><rect x="1" y="3" width="14" height="10" fill="var(--brand-green)"/><path d="M1 3l7 6 7-6" stroke="#fff" stroke-width="1.4" fill="none"/></svg>
        morgan@ridgelinebuild.com
      </li>
      <li class="contact__item">
        <svg class="contact__icon" viewBox="0 0 16 16" aria-hidden="true"><circle cx="8" cy="8" r="7" fill="none" stroke="var(--brand-green)" stroke-width="1.6"/><path d="M1 8h14M8 1c-3 4-3 10 0 14M8 1c3 4 3 10 0 14" stroke="var(--brand-green)" stroke-width="1.2" fill="none"/></svg>
        www.ridgelinebuild.com
      </li>
    </ul>
  </div>

  <div class="social-handle"><span class="social-handle__dot"></span>@ridgelinebuild</div>
</section>

<section class="card card--back" aria-label="Business card back">
  <svg class="card__bands" viewBox="0 0 640 366" aria-hidden="true">
    <polygon points="0,352 340,352 350,340 640,340 640,366 0,366" fill="var(--muted-grey)"/>
    <polygon points="340,366 392,300 640,300 640,366" fill="var(--brand-green)"/>
  </svg>

  <div class="company-name">
    <div class="company-name__title"><span class="company-name__mark"></span>RIDGELINE HOMES</div>
    <div class="company-name__sub">AND DEVELOPMENTS PTY LTD</div>
  </div>

  <div class="services">
    <h2 class="services__heading">Tailored Solutions for You:</h2>
    <ul class="services__list">
      <li class="services__item"><span class="services__bullet"></span>New Homes</li>
      <li class="services__item"><span class="services__bullet"></span>Carpentry</li>
      <li class="services__item"><span class="services__bullet"></span>Fences, Patios &amp; Pergolas</li>
      <li class="services__item"><span class="services__bullet"></span>Extensions, Renovations &amp; Bathrooms</li>
      <li class="services__item"><span class="services__bullet"></span>Decking, Carports, Sheds (Residential and Industrial)</li>
    </ul>
  </div>

  <div class="social-handle"><span class="social-handle__dot"></span>@ridgelinebuild</div>
</section>

</body>
</html>
```